Website for Apartment Rental in Prague

I would like to create designs of my website focused on luxury apartment rentals in Prague, Czech Republic. I created initial mock-ups, They are all attached. I need to design homepage and subpage. The mock-ups were created by combining elements from different websites that I liked but I need you to create a design that is unique and original. The attached files a only a guidance for the structure of the website but not for the design. Try to be creative.

Industry/Entity Type

Apartment

```html
<!DOCTYPE html>
<html lang="en">
<head>
<meta charset="utf-8">
<title>Velora Apartments Prague</title>
<link href="https://fonts.googleapis.com/css2?family=Barlow:ital,wght@0,400;0,500;0,600;0,700;1,400&family=Noto+Serif:ital,wght@1,400;1,700&display=swap" rel="stylesheet">
<style>
:root{
  --gold:#c2ae78;
  --ink:#222222;
  --text:#333333;
  --muted:#777777;
  --line:#e4e4e4;
  --paper:#ffffff;
  --mist:#f7f5f1;
  --chip:#ebebeb;
}
*{box-sizing:border-box;margin:0;padding:0}
html,body{width:1200px;height:2769px;overflow:hidden;background:var(--paper)}
body{position:relative;font-family:"Barlow",Arial,sans-serif;color:var(--text)}
.abs{position:absolute}

/* utility bar */
.utility{left:0;top:0;width:1200px;height:37px;border-bottom:1px solid var(--line);display:flex;justify-content:center;align-items:center;font-size:13px;color:#555}
.utility span{padding:0 14px;border-left:1px solid var(--line);display:flex;align-items:center;gap:6px;height:37px}
.utility span:first-child{border-left:none}
.utility svg{width:12px;height:12px}

/* brand */
.brand{left:0;top:37px;width:1200px;height:100px;display:flex;flex-direction:column;align-items:center;justify-content:center;gap:3px}
.brand-name,.brand-sub{font-size:16px;font-weight:600;letter-spacing:5px;color:var(--ink);line-height:20px}
.brand-rule{width:60px;height:2px;background:var(--gold);margin-top:5px}

/* navigation */
.nav{left:0;top:137px;width:1200px;height:38px;background:var(--ink);display:flex;justify-content:center}
.nav a{color:#fff;text-decoration:none;font-size:14.5px;font-weight:500;letter-spacing:.3px;padding:0 19px;line-height:38px;position:relative}
.nav a.active::before{content:"";position:absolute;left:0;right:0;top:-4px;height:4px;background:var(--gold)}

/* hero */
.hero{left:0;top:175px;width:1200px;height:423px;background:linear-gradient(100deg,#3b342e 0%,#7b6d60 22%,#c9bfb2 45%,#a79b8c 62%,#6d655e 82%,#4a4540 100%)}
.hero-title{left:0;top:340px;width:1200px;text-align:center;color:#fff;font-size:42px;font-weight:700;letter-spacing:.5px;line-height:50px}
.hero-tab{left:434px;top:559px;width:332px;height:39px;background:var(--gold);color:#fff;font-size:17px;display:flex;align-items:center;justify-content:center;border-radius:22px 22px 0 0}

/* booking */
.booking{left:0;top:598px;width:1200px;height:91px;background:var(--mist);border-bottom:1px solid var(--line)}
.field-label{top:612px;font-size:12.5px;color:#888}
.field{top:635px;height:37px;background:#fff;border:1px solid #dcdcdc;font-size:13px;color:#444;display:flex;align-items:center;padding-left:10px}
.field svg{position:absolute;right:8px;top:11px}
.check-btn{left:738px;top:635px;width:150px;height:37px;background:var(--gold);color:#fff;font-size:13px;font-weight:600;display:flex;align-items:center;justify-content:center}
.or{left:895px;top:645px;font-size:13px;color:#666}

/* intro */
.intro-rule{left:111px;top:764px;width:83px;height:2px;background:var(--gold)}
.intro-kicker{left:222px;top:750px;font-size:23px;letter-spacing:4px;color:#333;line-height:28px}
.intro-title{left:222px;top:780px;font-family:"Noto Serif",Georgia,serif;font-style:italic;font-weight:700;font-size:44px;line-height:52px;color:var(--ink)}
.intro-copy{left:222px;top:846px;width:362px;font-family:"Noto Serif",Georgia,serif;font-style:italic;font-size:15.5px;line-height:24px;color:#777}
.intro-copy p{margin-bottom:24px}
.designer-badge{left:222px;top:1108px;width:59px;height:59px;border:2px solid var(--gold);border-radius:50%}
.designer-badge svg{position:absolute;left:0;top:0}
.designer-text{left:301px;top:1116px;font-size:16px;line-height:22px;color:var(--ink);font-weight:600}
.designer-text span{font-weight:400;color:#666}
.frame{left:615px;top:759px;width:474px;height:384px;border-left:3px solid var(--gold);border-right:3px solid var(--gold);border-bottom:3px solid var(--gold)}
.frame-top{left:615px;top:759px;width:138px;height:3px;background:var(--gold)}
.frame-copy{left:687px;top:815px;width:330px;text-align:center;font-size:14.5px;line-height:24px;color:#666}

/* apartment cards */
.card{width:308px;height:456px}
.card .photo{position:absolute;left:0;top:0;width:308px;height:221px}
.card .price{position:absolute;right:10px;top:9px;height:33px;padding:0 11px;background:#fff;font-size:14px;color:var(--ink);display:flex;align-items:center;gap:4px}
.card .price i{font-style:italic}
.card .price b{font-weight:600}
.card .facts{position:absolute;left:0;top:221px;width:308px;height:37px;display:flex;gap:2px}
.card .facts span{flex:1;background:var(--chip);font-size:13px;color:#444;display:flex;align-items:center;justify-content:center}
.card h3{position:absolute;left:0;top:279px;width:308px;text-align:center;font-size:16.5px;font-weight:500;line-height:22px;color:var(--ink)}
.card .excerpt{position:absolute;left:0;top:341px;width:308px;text-align:center;font-size:15px;line-height:20px;color:#888}
.card .details{position:absolute;left:0;top:380px;width:308px;height:34px;background:var(--ink);color:#fff;font-size:14px;font-weight:600;display:flex;align-items:center;justify-content:center}
.card .book{position:absolute;left:0;top:423px;width:308px;height:33px;background:var(--gold);color:#fff;font-size:14px;font-weight:500;display:flex;align-items:center;justify-content:center}

/* need to know */
.ntk-title{left:0;top:2237px;width:1200px;text-align:center;font-size:25px;line-height:30px;letter-spacing:4px;color:#333}
.ntk{width:300px;text-align:center}
.ntk svg{display:block;margin:0 auto}
.ntk h4{font-size:17px;font-weight:600;line-height:22px;color:var(--ink);margin-top:20px}
.ntk p{font-size:14.5px;color:#777;line-height:24px;margin-top:14px}

/* footer */
.footer{left:0;top:2514px;width:1200px;height:255px;background:var(--ink)}
.f-head{font-size:19px;line-height:24px;color:#fff;font-weight:500}
.f-small{font-size:12.5px;line-height:18px;color:#ccc}
.f-phone{font-size:27px;line-height:32px;color:#fff;font-weight:500}
.f-links{font-size:13px;line-height:27px;color:#ccc}
.social{display:flex;gap:4px}
.social span{width:34px;height:34px;border:1.5px solid #bbb;border-radius:50%}
.message{left:864px;top:2727px;width:223px;height:42px;background:var(--gold);border-radius:8px 8px 0 0;color:#fff;font-size:15px;font-weight:600;display:flex;align-items:center;justify-content:center;gap:10px}
</style>
</head>
<body>

<div class="abs utility">
  <span><svg viewBox="0 0 12 12"><rect x="2" y="2" width="8" height="8" fill="none" stroke="#888"/></svg>Our Hospitality</span>
  <span><svg viewBox="0 0 12 12"><path d="M2 11V1h7l-2 3 2 3H2" fill="none" stroke="#888"/></svg>Discover Prague</span>
  <span><svg viewBox="0 0 12 12"><rect x="1" y="3" width="10" height="7" fill="none" stroke="#888"/><path d="M1 3l5 4 5-4" fill="none" stroke="#888"/></svg>reservation@velorastays.com</span>
  <span><svg viewBox="0 0 12 12"><path d="M3 1l2 3-1 1c1 2 2 3 3 3l1-1 3 2-1 2C5 11 1 7 1 2z" fill="#888"/></svg>420 600 318 452</span>
  <span>En ▾</span>
</div>

<div class="abs brand">
  <div class="brand-name">VELORA</div>
  <div class="brand-sub">PRAGUE</div>
  <div class="brand-rule"></div>
</div>

<nav class="abs nav">
  <a class="active">APARTMENTS</a><a>LOCATION</a><a>SERVICES</a><a>GALLERY</a><a>NEWS</a><a>EXCLUSIVE OFFERS &amp; TOURS</a><a>FOR FAMILIES</a><a>CONTACT US</a>
</nav>

<div class="abs hero" role="img" aria-label="Photo of a bright modern apartment living room with a beige sofa and wood floor"></div>
<div class="abs hero-title">BEING HOME IN PRAGUE</div>
<div class="abs hero-tab">Official Site - Best Price Guaranteed</div>

<div class="abs booking"></div>
<div class="abs field-label" style="left:127px">Check in date</div>
<div class="abs field-label" style="left:257px">Check out date</div>
<div class="abs field-label" style="left:386px">Adults</div>
<div class="abs field-label" style="left:449px">Children</div>
<div class="abs field-label" style="left:511px">Infants</div>
<div class="abs field-label" style="left:574px">Promotional code</div>
<div class="abs field" style="left:127px;width:120px">11/17/2017<svg width="16" height="15" viewBox="0 0 16 15"><rect x="1" y="2" width="14" height="12" fill="none" stroke="#999"/><path d="M1 6h14M5 0v4M11 0v4" stroke="#999"/></svg></div>
<div class="abs field" style="left:257px;width:118px">11/18/2017<svg width="16" height="15" viewBox="0 0 16 15"><rect x="1" y="2" width="14" height="12" fill="none" stroke="#999"/><path d="M1 6h14M5 0v4M11 0v4" stroke="#999"/></svg></div>
<div class="abs field" style="left:386px;width:55px">2<svg width="8" height="14" viewBox="0 0 8 14"><path d="M0 0v14" stroke="#ddd"/><path d="M3 6l2 3 2-3z" fill="#999"/></svg></div>
<div class="abs field" style="left:449px;width:55px">0<svg width="8" height="14" viewBox="0 0 8 14"><path d="M0 0v14" stroke="#ddd"/><path d="M3 6l2 3 2-3z" fill="#999"/></svg></div>
<div class="abs field" style="left:511px;width:56px">0<svg width="8" height="14" viewBox="0 0 8 14"><path d="M0 0v14" stroke="#ddd"/><path d="M3 6l2 3 2-3z" fill="#999"/></svg></div>
<div class="abs field" style="left:574px;width:155px"></div>
<div class="abs check-btn">CHECK AVAILABILITY</div>
<div class="abs or">OR</div>
<div class="abs field" style="left:923px;width:148px;font-size:12.5px">Select Rental Unit<svg width="8" height="14" viewBox="0 0 8 14"><path d="M0 0v14" stroke="#ddd"/><path d="M3 6l2 3 2-3z" fill="#999"/></svg></div>

<div class="abs intro-rule"></div>
<div class="abs intro-kicker">A DIFFERENT VISION OF</div>
<div class="abs intro-title">Travelling</div>
<div class="abs intro-copy">
  <p>Something spectacular has arrived in the heart of europe.</p>
  <p>Steps from old town, this rental experience is curated with world-class amenities, exemplary style and a level of convenience you have to experience to believe.</p>
  <p>Experience the different vision of luxury in center of prague.</p>
</div>
<div class="abs designer-badge"><svg width="55" height="55" viewBox="0 0 55 55"><path d="M21 15h13l4 14H17z" fill="none" stroke="#c2ae78" stroke-width="2"/><path d="M27.5 29v9M21 40h13" stroke="#c2ae78" stroke-width="2"/></svg></div>
<div class="abs designer-text">Interiors Designed<br>by <span>Velora</span></div>

<div class="abs frame"></div>
<div class="abs frame-top"></div>
<div class="abs frame-copy">Velora apartments offers short term and as well as long term options in our studio apartments and our one bedroom apartment homes. Our luxurious apartments and high quality customer service have allowed us to dominate the Prague apartment market with a proven track record. Our years of experience and knowledge have made us a premier apartment rental company as we continue to stress the importance of servicing individuals and corporations who are seeking the finest accommodations.</div>

<div class="abs card" style="left:111px;top:1237px">
  <div class="photo" role="img" aria-label="Photo of a white open-plan living room with a staircase" style="background:linear-gradient(160deg,#e9e6e1,#b8a792 70%,#7a5a3e)"></div>
  <div class="price"><i>From</i><b>150 USD</b></div>
  <div class="facts"><span>1 Bedroom</span><span>Max 4 People</span></div>
  <h3>Brand New Luxury Living<br>Stunning Contemporary Design</h3>
  <div class="excerpt">The 22nd issue is dedicated to colors...</div>
  <div class="details">DETAILS</div><div class="book">BOOK NOW</div>
</div>
<div class="abs card" style="left:445px;top:1237px">
  <div class="photo" role="img" aria-label="Photo of a grey living room with a bright window" style="background:linear-gradient(160deg,#6c6c70,#c9c2b8 50%,#5b4f46)"></div>
  <div class="price"><i>From</i><b>150 USD</b></div>
  <div class="facts"><span>1 Bedroom</span><span>Max 4 People</span></div>
  <h3>Brand New Luxury Living<br>Stunning Contemporary Design</h3>
  <div class="excerpt">The 22nd issue is dedicated to colors...</div>
  <div class="details">DETAILS</div><div class="book">BOOK NOW</div>
</div>
<div class="abs card" style="left:779px;top:1237px">
  <div class="photo" role="img" aria-label="Photo of a warm wood-panelled bedroom at night" style="background:linear-gradient(160deg,#3a2414,#a46a34 50%,#1d1a1a)"></div>
  <div class="price"><i>From</i><b>150 USD</b></div>
  <div class="facts"><span>1 Bedroom</span><span>Max 4 People</span></div>
  <h3>Brand New Luxury Living<br>Stunning Contemporary Design</h3>
  <div class="excerpt">The 22nd issue is dedicated to colors...</div>
  <div class="details">DETAILS</div><div class="book">BOOK NOW</div>
</div>
<div class="abs card" style="left:111px;top:1719px">
  <div class="photo" role="img" aria-label="Photo of a bright loft living area with wood floor" style="background:linear-gradient(160deg,#ede9e3,#c7b59b 55%,#8b6a48)"></div>
  <div class="price"><i>From</i><b>150 USD</b></div>
  <div class="facts"><span>1 Bedroom</span><span>Max 4 People</span></div>
  <h3>Brand New Luxury Living<br>Stunning Contemporary Design</h3>
  <div class="excerpt">The 22nd issue is dedicated to colors...</div>
  <div class="details">DETAILS</div><div class="book">BOOK NOW</div>
</div>
<div class="abs card" style="left:445px;top:1719px">
  <div class="photo" role="img" aria-label="Photo of a lounge with a floating staircase and fireplace" style="background:linear-gradient(160deg,#d8d4ce,#f1efec 45%,#6b5140)"></div>
  <div class="price"><i>From</i><b>150 USD</b></div>
  <div class="facts"><span>1 Bedroom</span><span>Max 4 People</span></div>
  <h3>Brand New Luxury Living<br>Stunning Contemporary Design</h3>
  <div class="excerpt">The 22nd issue is dedicated to colors...</div>
  <div class="details">DETAILS</div><div class="book">BOOK NOW</div>
</div>
<div class="abs card" style="left:779px;top:1719px">
  <div class="photo" role="img" aria-label="Photo of a modern living room with dark walls and wood floor" style="background:linear-gradient(160deg,#8fa3b6,#4b4d52 50%,#a06a35)"></div>
  <div class="price"><i>From</i><b>150 USD</b></div>
  <div class="facts"><span>1 Bedroom</span><span>Max 4 People</span></div>
  <h3>Brand New Luxury Living<br>Stunning Contemporary Design</h3>
  <div class="excerpt">The 22nd issue is dedicated to colors...</div>
  <div class="details">DETAILS</div><div class="book">BOOK NOW</div>
</div>

<div class="abs ntk-title">NEED TO KNOW</div>
<div class="abs ntk" style="left:116px;top:2305px">
  <svg width="56" height="60" viewBox="0 0 56 60" fill="none" stroke="#c2ae78" stroke-width="2"><path d="M6 58V20h16v38M22 58V4h18v54M40 58V26h12v32M2 58h52"/><path d="M28 12h6M28 20h6M28 28h6M28 36h6M11 28h6M11 36h6M44 34h4M44 42h4"/></svg>
  <h4>Apartments</h4>
  <p>Also avaliable to rent all the apartmets<br>together for companies or larger groups.</p>
</div>
<div class="abs ntk" style="left:450px;top:2305px">
  <svg width="56" height="60" viewBox="0 0 56 60" fill="none" stroke="#c2ae78" stroke-width="2"><rect x="10" y="16" width="36" height="36" rx="3"/><path d="M21 16V6h14v10M20 24v22M28 24v22M36 24v22M4 56h48"/></svg>
  <h4>Check-Out</h4>
  <p>12 noon; earliest check-in, 3pm- both are<br>flexible, by arrangement.</p>
</div>
<div class="abs ntk" style="left:784px;top:2305px">
  <svg width="60" height="60" viewBox="0 0 60 60" fill="none" stroke="#c2ae78" stroke-width="2"><circle cx="30" cy="30" r="27"/><path d="M37 21c-2-3-5-4-8-4-4 0-7 2-7 6 0 8 16 5 16 13 0 4-4 6-8 6-4 0-7-2-8-5M30 13v34"/></svg>
  <h4>Rates</h4>
  <p>Prices from <b style="color:#333">150 USD</b> per night.<br>Including tax.</p>
</div>

<footer class="abs footer"></footer>
<div class="abs f-head" style="left:111px;top:2552px">Contact Us</div>
<div class="abs f-small" style="left:111px;top:2587px">Velora Apartments Prague<br>228, lorem ipsum dolor sit,<br>osis amet it 85965</div>
<div class="abs f-phone" style="left:111px;top:2670px">420 600 318 452</div>
<div class="abs f-small" style="left:111px;top:2702px">reservation@velorastays.com</div>
<div class="abs f-head" style="left:445px;top:2552px">Quick Links</div>
<div class="abs f-links" style="left:445px;top:2583px">Apartments<br>Location<br>Services<br>Gallery<br>News</div>
<div class="abs f-links" style="left:561px;top:2583px">Exclusive Offers &amp; Tours<br>For Families<br>Contact Us</div>
<div class="abs f-head" style="left:862px;top:2552px">Stay Connected</div>
<div class="abs social" style="left:864px;top:2590px"><span></span><span></span><span></span><span></span><span></span></div>
<div class="abs f-small" style="left:864px;top:2662px">© 2017 Velora Apartments Prague.</div>
<div class="abs message"><svg width="20" height="16" viewBox="0 0 20 16"><path d="M2 1h16v10H8l-4 4v-4H2z" fill="#fff"/></svg>Please Leave A Message</div>

</body>
</html>
```